Heronwick Lodge Sign

Heronwick Lodge is a lake resort in Branson, MO
This resort used to have 66 units however the resort was sold in sections. I own the part of the resort that has all the amenities listed on the attached file. We need an updated sign and also billboard.
On a sign like this should be include a phone number?

```html
<!DOCTYPE html>
<html lang="en">
<head>
<meta charset="utf-8">
<title>Heronwick Lodge Sign</title>
<link href="https://fonts.googleapis.com/css2?family=Jost:wght@500&display=swap" rel="stylesheet">
<style>
  :root {
    --backdrop: #0b3343;
    --sign: #e6f3ea;
    --ink: #111111;
    --white: #ffffff;
    --blue: #2f4aa0;
    --orange: #f0922e;
    --yellow: #fff200;
    --green: #7cc242;
    --teal: #00a39a;
    --emerald: #0aab4e;
    --red-orange: #e85a30;
    --lime: #a6cf3a;
    --crimson: #d61f34;
    --purple: #9d4597;
    --red: #d9252d;
  }
  * { box-sizing: border-box; margin: 0; padding: 0; }
  html, body {
    width: 1200px; height: 848px; overflow: hidden;
    background: var(--backdrop);
    font-family: "Jost", sans-serif;
  }
  .sign {
    position: absolute; left: 200px; top: 64px;
    width: 801px; height: 720px;
    background: var(--sign);
    border: 1px solid #000;
    overflow: hidden;
  }
  .brand {
    position: absolute; left: 79px; top: 9px;
    width: 642px; height: 233px;
    display: flex; align-items: center; justify-content: center;
  }
  .brand-name {
    font-weight: 500; font-size: 84px; color: var(--ink);
    letter-spacing: 1px;
  }
  .amenities {
    position: absolute; left: 57px; top: 270px;
    display: grid; grid-template-columns: 331px 331px;
    column-gap: 24px; row-gap: 6px;
  }
  .amenity {
    height: 42px; border-radius: 8px;
    display: flex; align-items: center; justify-content: center;
    color: var(--white); font-weight: 500; font-size: 24px;
    text-shadow: 2px 2px 3px rgba(0,0,0,.45);
    white-space: nowrap;
  }
  .amenity.small { font-size: 20px; }
  .amenity.smaller { font-size: 19px; }
  .row-1 { background: linear-gradient(90deg, var(--blue), var(--orange)); }
  .row-2 { background: linear-gradient(90deg, var(--yellow), var(--green)); }
  .row-3 { background: linear-gradient(90deg, var(--teal), var(--emerald)); }
  .row-4 { background: linear-gradient(90deg, var(--orange), var(--red-orange)); }
  .row-5 { background: linear-gradient(90deg, var(--lime), var(--crimson)); }
  .row-6 { background: linear-gradient(90deg, var(--yellow), var(--purple)); }
  .row-7 { background: linear-gradient(90deg, var(--emerald), var(--red-orange)); }
  .row-8 { background: linear-gradient(90deg, var(--red), var(--emerald)); }
  .contact-band {
    position: absolute; top: 668px; height: 52px;
    display: flex; align-items: center; justify-content: center;
    color: var(--white); font-weight: 500; font-size: 30px;
    background: linear-gradient(90deg, var(--teal), #0a6fb8 55%, var(--emerald));
  }
  .address { left: 0; width: 420px; clip-path: polygon(54px 0, 100% 0, calc(100% - 54px) 100%, 0 100%); }
  .website { left: 376px; width: 421px; background: linear-gradient(90deg, var(--teal), #0a8fb0 50%, var(--emerald)); clip-path: polygon(54px 0, 100% 0, calc(100% - 54px) 100%, 0 100%); }
</style>
</head>
<body>
  <div class="sign">
    <div class="brand">
      <span class="brand-name">Heronwick Lodge</span>
    </div>

    <div class="amenities">
      <div class="amenity row-1">Direct Lake access</div>
      <div class="amenity row-1 small">1-3 Bedroom Vacation Rentals</div>
      <div class="amenity row-2">Swim Decks</div>
      <div class="amenity row-2">Dining Hall</div>
      <div class="amenity row-3">Slip Rentals</div>
      <div class="amenity row-3">Game Room</div>
      <div class="amenity row-4">Boat Rentals</div>
      <div class="amenity row-4">Children Activities</div>
      <div class="amenity row-5">Indoor Pool</div>
      <div class="amenity row-5">Pet Friendly</div>
      <div class="amenity row-6">Golf Carts</div>
      <div class="amenity row-6">Gift Store</div>
      <div class="amenity row-7">Pontoon Boats</div>
      <div class="amenity row-7">Outdoor Games</div>
      <div class="amenity row-8">Kayak - Paddleboards</div>
      <div class="amenity row-8 smaller">Family Reunions - Large Groups</div>
    </div>

    <div class="contact-band address">28 Willow Bend Lane</div>
    <div class="contact-band website">heronwicklodge.com</div>
  </div>
</body>
</html>
```